Halvern Properties Business Cards

I would like a business card that includes myself and my partner.
Includes: Logo, office #, email, website, our names, our numbers and possibly the address. I would also like the logo to be embossed and the card to be horizontal.
There is a photo of our yard signs to give you an idea of the colors of our business.

Target Market(s)

Everyone in real estate market.
We are in a rural area. Our clientele are from all socioeconomic backgrounds.

Industry/Entity Type

Real Estate Agent

Contact Information for Business Card

Company Name: Halvern Properties
Our Names, Titles & Cell #'s : Marla Halvern-Broker (555).316.4827, Tessa Halvern-Realtor (555).627.9154
Office #: (555).841.2600
Website: halvernproperties-example.com
Joint Email: halvern@halvernproperties-example.com
Office Address: 518B W. Cottonwell Ave.
Fallowmere, QX. 70999

Font styles to use
Serif

Requirements
Must have
• HORIZONTAL, Logo, Myself and my partners names, Our cell #'s, our office #, our website, our email address
Nice to have
• Embossed logo, office address, our titles.

```html
<!DOCTYPE html>
<html lang="en">
<head>
<meta charset="utf-8">
<title>Halvern Properties — Business Card</title>
<link rel="stylesheet" href="https://fonts.googleapis.com/css2?family=Marcellus&family=Source+Sans+3:wght@400&display=swap">
<style>
  :root{
    --violet:#3a0ee8;
    --navy:#22078c;
    --cream:#fcfcbd;
    --aqua:#8ff7ef;
    --logo-ink:#2c1a7a;
    --white:#ffffff;
    --photo-sky:#c9d9e6;
    --photo-house:#7d8791;
    --photo-ground:#5f6a55;
  }
  *{margin:0;padding:0;box-sizing:border-box}
  html,body{width:1200px;height:720px;overflow:hidden;background:#ffffff}
  .card{position:relative;width:1200px;height:720px;overflow:hidden;background:var(--navy)}
  .band-top{position:absolute;left:0;top:0;width:1200px;height:41px;background:var(--violet)}
  .header{position:absolute;left:0;top:41px;width:1200px;height:249px;background:var(--cream)}
  .stripe{position:absolute;left:0;top:667px;width:1200px;height:13px;background:var(--cream)}
  .band-bottom{position:absolute;left:0;top:680px;width:1200px;height:40px;background:var(--violet)}
  .brand{position:absolute;left:0;top:41px;width:1200px;height:249px;display:flex;align-items:center;justify-content:center;gap:22px}
  .brand-mark{width:64px;height:64px;border-radius:50%;background:var(--logo-ink)}
  .brand-name{font-family:"Marcellus",serif;font-size:62px;color:var(--logo-ink);letter-spacing:2px;line-height:1}
  .visual{position:absolute;left:0;top:0}
  .contacts{position:absolute;left:74px;top:322px;color:var(--white);font-family:"Source Sans 3",sans-serif;font-weight:400;white-space:nowrap}
  .agent{margin-bottom:14px}
  .agent-name,.agent-title,.agent-phone{line-height:30px}
  .agent-name{font-size:33px;letter-spacing:-1px}
  .agent-title{font-size:23px;letter-spacing:-0.5px}
  .agent-phone{font-size:31px;letter-spacing:-0.3px}
  .office{margin-top:31px;font-size:21px;line-height:24px}
</style>
</head>
<body>
<div class="card">
  <div class="band-top"></div>
  <div class="header"></div>

  <div class="brand">
    <span class="brand-mark"></span>
    <span class="brand-name">Halvern Properties</span>
  </div>

  <svg class="visual" width="1200" height="720" viewBox="0 0 1200 720">
    <defs>
      <linearGradient id="house-photo" x1="0" y1="0" x2="0" y2="1">
        <stop offset="0" stop-color="var(--photo-sky)"/>
        <stop offset="0.45" stop-color="var(--photo-house)"/>
        <stop offset="1" stop-color="var(--photo-ground)"/>
      </linearGradient>
    </defs>
    <polygon class="accent-wedge" points="581,290 971,290 894,389" fill="var(--aqua)"/>
    <polygon class="house-photo" role="img" aria-label="Photo of a two-storey suburban house with grey shingle roofs and white trim"
      points="971,290 1200,290 1200,645 695,645" fill="url(#house-photo)"/>
  </svg>

  <div class="contacts">
    <div class="agent">
      <div class="agent-name">MARLA HALVERN</div>
      <div class="agent-title">Broker</div>
      <div class="agent-phone">(555).316.4827</div>
    </div>
    <div class="agent">
      <div class="agent-name">TESSA HALVERN</div>
      <div class="agent-title">Realtor</div>
      <div class="agent-phone">(555).627.9154</div>
    </div>
    <div class="office">
      <div>Office #: (555).841.2600</div>
      <div>518B W. Cottonwell Ave. Fallowmere, QX. 70999</div>
      <div>Website: www.halvernproperties-example.com</div>
      <div>Email: halvern@halvernproperties-example.com</div>
    </div>
  </div>

  <div class="stripe"></div>
  <div class="band-bottom"></div>
</div>
</body>
</html>
```